Bookmarks for teachers and high school students - Range of 6

We are after a range of 6 bookmarks to use as hand outs to schools and students that we supply books and other school resources to.

Each bookmark is to have an inspirational quote on it and be a different color. You can decide color and background texture.

The back of them shall all be black or white, so just fronts needed. We want these 6 bookmarks to be similar in design, so they look like a matching range. And be nice enough that teachers and students will pick one to use.

We also want our logo to be on the bookmark, maybe just tucked down the bottom and our web address showing please - www.tarleby.com.au

Attached is the 6 quotes we want to use and an examples of the type of font I would like to see. But each a different font ..Also attached is our logo.

I think simple and smart may be best, but see what you come up with as I am also open to making them funky for students (if possible)

The print size of each bookmark is 40mm by 210mm

Target Market(s)

teachers and high school students

Industry/Entity Type

School

Requirements
Must have
• be eye catching

```html
<!DOCTYPE html>
<html lang="en">
<head>
<meta charset="utf-8">
<title>Tarleby Education Bookmark Range</title>
<link rel="stylesheet" href="https://fonts.googleapis.com/css2?family=Anton&family=Cinzel:wght@400;700&family=Great+Vibes&family=Montserrat:wght@500&family=Open+Sans:wght@400;600;700;800&family=Playfair+Display:wght@400;700;900&display=swap">
<style>
  :root {
    --stage: #d4d5d7;
    --ink: #333132;
    --paper: #ffffff;
    --red: #e93438;
    --coral: #f4866f;
    --green: #a9cf46;
    --blue: #7098c4;
    --grey-fill: #ececec;
    --grey-line: #555555;
  }
  html, body {
    margin: 0;
    width: 1200px;
    height: 1000px;
    overflow: hidden;
    background: var(--stage);
  }
  .range {
    position: relative;
    width: 1200px;
    height: 1000px;
  }
  .bookmark {
    position: absolute;
    top: 65px;
    width: 165px;
    height: 870px;
    box-shadow: 0 2px 6px rgba(0,0,0,0.25);
  }
  .bookmark--red { left: 318px; }
  .bookmark--green { left: 517px; }
  .bookmark--blue { left: 716px; }
  .bookmark svg { display: block; }

  .band { fill: var(--ink); }
  .paper { fill: var(--paper); }
  .hole { fill: var(--paper); }
  .red .tint { fill: var(--red); }
  .green .tint { fill: var(--green); }
  .blue .tint { fill: var(--blue); }

  text { text-anchor: middle; }
  .serif { font-family: "Playfair Display", serif; }
  .serif-heavy { font-family: "Playfair Display", serif; font-weight: 900; }
  .script { font-family: "Great Vibes", cursive; }
  .roman { font-family: "Cinzel", serif; }
  .condensed { font-family: "Anton", sans-serif; }
  .sans { font-family: "Open Sans", sans-serif; }
  .sans-bold { font-family: "Open Sans", sans-serif; font-weight: 800; }
  .on-tint { fill: var(--paper); }
  .on-paper { fill: var(--ink); }
  .quote-accent--red { fill: var(--coral); stroke: #fbd0c5; stroke-width: 0.8; }
  .quote-outline { fill: var(--grey-fill); stroke: var(--grey-line); stroke-width: 1.2; }

  .scribble { fill: none; stroke-width: 3; }
  .scribble--red { stroke: var(--red); }
  .scribble--green { stroke: var(--green); stroke-width: 4; }
  .scribble--blue { stroke: var(--blue); }

  .attribution-rule { stroke: var(--ink); stroke-width: 0.8; }
  .attribution { font-family: "Playfair Display", serif; font-size: 8.5px; fill: var(--ink); }
  .brand-name { font-family: "Montserrat", sans-serif; font-weight: 500; fill: var(--ink); }
  .brand-sub { font-family: "Montserrat", sans-serif; font-weight: 500; fill: var(--ink); text-anchor: end; }
  .web { font-family: "Open Sans", sans-serif; font-weight: 600; font-size: 10.5px; fill: var(--paper); }
</style>
</head>
<body>
<main class="range">

  <article class="bookmark bookmark--red red">
    <svg width="165" height="870" viewBox="0 0 165 870">
      <rect class="paper" x="0" y="0" width="165" height="870"/>
      <rect class="tint" x="0" y="53" width="165" height="310"/>
      <rect class="band" x="0" y="0" width="165" height="53"/>
      <polygon class="band" points="0,53 82.5,117 165,53"/>
      <circle class="tint" cx="82.5" cy="42" r="20"/>
      <circle class="hole" cx="82.5" cy="42" r="10"/>

      <text class="serif on-tint" x="82.5" y="146" font-size="17">IT</text>
      <text class="serif on-tint" x="82.5" y="168" font-size="17">DOESN’T</text>
      <text class="serif on-tint" x="82.5" y="190" font-size="17">MATTER</text>
      <text class="serif-heavy quote-accent--red" x="82.5" y="234" font-size="40" textLength="124" lengthAdjust="spacingAndGlyphs">WHO</text>
      <text class="serif-heavy quote-accent--red" x="82.5" y="296" font-size="68" textLength="140" lengthAdjust="spacingAndGlyphs">WE</text>
      <text class="serif-heavy quote-accent--red" x="82.5" y="340" font-size="40" textLength="106" lengthAdjust="spacingAndGlyphs">ARE</text>

      <text class="serif on-paper" x="82.5" y="404" font-size="18">WHAT</text>
      <text class="serif on-paper" x="82.5" y="426" font-size="18">MATTERS</text>
      <text class="serif on-paper" x="82.5" y="446" font-size="15">IS</text>
      <text class="serif-heavy quote-outline" x="82.5" y="500" font-size="54" textLength="146" lengthAdjust="spacingAndGlyphs">OUR</text>
      <text class="serif-heavy quote-outline" x="82.5" y="546" font-size="44" textLength="130" lengthAdjust="spacingAndGlyphs">PLAN</text>
      <ellipse class="scribble scribble--red" cx="82" cy="505" rx="74" ry="65" transform="rotate(-8 82 505)"/>

      <line class="attribution-rule" x1="0" y1="640" x2="26" y2="640"/>
      <line class="attribution-rule" x1="139" y1="640" x2="165" y2="640"/>
      <text class="attribution" x="82.5" y="643">THE QUIET HARBOUR</text>

      <text class="brand-name" x="82.5" y="726" font-size="24" textLength="136" lengthAdjust="spacingAndGlyphs">TARLEBY</text>
      <text class="brand-sub" x="150" y="740" font-size="7.5" letter-spacing="0.8">EDUCATION</text>

      <polygon class="band" points="0,817 82.5,753 165,817"/>
      <rect class="band" x="0" y="817" width="165" height="53"/>
      <text class="web" x="82.5" y="848" textLength="137" lengthAdjust="spacing">www.tarleby.com.au</text>
    </svg>
  </article>

  <article class="bookmark bookmark--green green">
    <svg width="165" height="870" viewBox="0 0 165 870">
      <rect class="paper" x="0" y="0" width="165" height="870"/>
      <rect class="tint" x="0" y="53" width="165" height="310"/>
      <rect class="band" x="0" y="0" width="165" height="53"/>
      <polygon class="band" points="0,53 82.5,117 165,53"/>
      <circle class="tint" cx="82.5" cy="42" r="20"/>
      <circle class="hole" cx="82.5" cy="42" r="10"/>

      <text class="script on-paper" x="82.5" y="224" font-size="44">Dreams</text>
      <text class="roman on-paper" x="82.5" y="254" font-size="17">CAN</text>
      <text class="roman on-paper" x="82.5" y="288" font-size="30">COME</text>
      <text class="roman on-paper" x="82.5" y="334" font-size="44" font-weight="700">TRUE</text>

      <ellipse class="scribble scribble--green" cx="84" cy="490" rx="76" ry="70" transform="rotate(-12 84 490)"/>
      <text class="roman on-paper" x="82.5" y="408" font-size="17">IF WE HAVE</text>
      <text class="roman on-paper" x="82.5" y="430" font-size="14">THE</text>
      <text class="condensed on-paper" x="82.5" y="474" font-size="42" textLength="146" lengthAdjust="spacingAndGlyphs">COURAGE</text>
      <text class="condensed on-paper" x="82.5" y="504" font-size="22">TO</text>
      <text class="condensed on-paper" x="82.5" y="546" font-size="42" textLength="120" lengthAdjust="spacingAndGlyphs">PURSUE</text>
      <text class="roman on-paper" x="82.5" y="570" font-size="15">THEM</text>

      <line class="attribution-rule" x1="0" y1="640" x2="36" y2="640"/>
      <line class="attribution-rule" x1="129" y1="640" x2="165" y2="640"/>
      <text class="attribution" x="82.5" y="643">MARGO ELLISON</text>

      <text class="brand-name" x="82.5" y="726" font-size="24" textLength="136" lengthAdjust="spacingAndGlyphs">TARLEBY</text>
      <text class="brand-sub" x="150" y="740" font-size="7.5" letter-spacing="0.8">EDUCATION</text>

      <polygon class="band" points="0,817 82.5,753 165,817"/>
      <rect class="band" x="0" y="817" width="165" height="53"/>
      <text class="web" x="82.5" y="848" textLength="137" lengthAdjust="spacing">www.tarleby.com.au</text>
    </svg>
  </article>

  <article class="bookmark bookmark--blue blue">
    <svg width="165" height="870" viewBox="0 0 165 870">
      <rect class="paper" x="0" y="0" width="165" height="870"/>
      <rect class="tint" x="0" y="53" width="165" height="310"/>
      <rect class="band" x="0" y="0" width="165" height="53"/>
      <polygon class="band" points="0,53 82.5,117 165,53"/>
      <circle class="tint" cx="82.5" cy="42" r="20"/>
      <circle class="hole" cx="82.5" cy="42" r="10"/>

      <text class="sans on-tint" x="82.5" y="170" font-size="18">THOSE THAT</text>
      <text class="sans-bold on-tint" x="82.5" y="218" font-size="40">DON’T</text>
      <text class="sans-bold on-tint" x="82.5" y="264" font-size="36" textLength="136" lengthAdjust="spacingAndGlyphs">BELIEVE</text>
      <text class="sans on-tint" x="82.5" y="292" font-size="16">IN</text>
      <polygon class="hole" points="112,282 114,288 120,288 115,292 117,298 112,294 107,298 109,292 104,288 110,288"/>
      <text class="roman on-tint" x="82.5" y="342" font-size="38" textLength="132" lengthAdjust="spacingAndGlyphs">MAGIC</text>

      <ellipse class="scribble scribble--blue" cx="82" cy="490" rx="70" ry="60" transform="rotate(-6 82 490)"/>
      <ellipse class="scribble scribble--blue" cx="84" cy="494" rx="64" ry="56" transform="rotate(10 84 494)"/>
      <text class="sans on-paper" x="82.5" y="418" font-size="28">WILL</text>
      <text class="sans-bold on-paper" x="82.5" y="470" font-size="40" textLength="136" lengthAdjust="spacingAndGlyphs">NEVER</text>
      <text class="sans-bold on-paper" x="82.5" y="524" font-size="40">FIND</text>
      <text class="sans on-paper" x="82.5" y="568" font-size="22">IT</text>

      <line class="attribution-rule" x1="0" y1="640" x2="40" y2="640"/>
      <line class="attribution-rule" x1="125" y1="640" x2="165" y2="640"/>
      <text class="attribution" x="82.5" y="643">PETER STRAND</text>

      <text class="brand-name" x="82.5" y="726" font-size="24" textLength="136" lengthAdjust="spacingAndGlyphs">TARLEBY</text>
      <text class="brand-sub" x="150" y="740" font-size="7.5" letter-spacing="0.8">EDUCATION</text>

      <polygon class="band" points="0,817 82.5,753 165,817"/>
      <rect class="band" x="0" y="817" width="165" height="53"/>
      <text class="web" x="82.5" y="848" textLength="137" lengthAdjust="spacing">www.tarleby.com.au</text>
    </svg>
  </article>

</main>
</body>
</html>
```